Stationery for a recruitment agency

We need a logo, letterhead and business card design that will represent our 28 year old recruitment agency that was started by us in 1989 here in Perth (Australia). We target professional companies that want us to do their sourcing and screening of candidates.

Primarily our clients like to use agencies as we have greater access to candidates than they do. Our imagery needs to reflect strength and that we are serious about recruiting and systems, and that we can meet their people supply needs both now and into the future.

Once we place a person into a job we also help manage their performance as we do Performance Appraisals and link the goals of the company to the KPI's (Key Performance Indicators) of the individual.

Target Market(s)

Corporate companies with 50+ employees

Industry/Entity Type

Recruitment

Font styles to use
Serif
Sans Serif

Colors

Designer to choose colors to be used in the design.

Requirements
Must have
• Our business name is Harbourline Staffing and must be used in the logo
Nice to have
• Having been around since 1989 is a pretty big thing in such a competitive business.

```html
<!DOCTYPE html>
<html lang="en">
<head>
<meta charset="utf-8">
<title>Harbourline Staffing — Stationery</title>
<link rel="stylesheet" href="https://fonts.googleapis.com/css2?family=Crimson+Text:ital,wght@0,400;1,400&display=swap">
<style>
  :root {
    --brand-red: #c01d2e;
    --ink: #222222;
    --paper: #ffffff;
    --mist: #f1f1f1;
    --backdrop: #e9e6e3;
    --serif: "Crimson Text", Georgia, serif;
  }
  * { box-sizing: border-box; margin: 0; padding: 0; }
  html, body { width: 1200px; height: 926px; overflow: hidden; background: var(--backdrop); }
  .canvas { position: relative; width: 1200px; height: 926px; }

  .sheet { position: absolute; width: 430px; height: 608px; box-shadow: 0 6px 18px rgba(0,0,0,.18); }
  .letterhead { left: 60px; top: 36px; background: var(--paper); }
  .folder { left: 520px; top: 36px; background: var(--brand-red); }

  .wordmark { display: flex; align-items: center; gap: 10px; font-family: var(--serif); font-weight: 400; line-height: 1; white-space: nowrap; }
  .wordmark-dot { flex: none; border-radius: 50%; }

  .letterhead-logo { position: absolute; top: 44px; left: 0; right: 0; display: flex; justify-content: center; }
  .letterhead-logo .wordmark { color: var(--ink); font-size: 26px; }
  .letterhead-logo .wordmark-dot { width: 22px; height: 22px; background: var(--brand-red); }

  .letterhead-watermark { position: absolute; top: 250px; left: 0; right: 0; display: flex; justify-content: center; opacity: .09; }
  .letterhead-watermark .wordmark { color: var(--brand-red); font-size: 40px; gap: 12px; }
  .letterhead-watermark .wordmark-dot { width: 36px; height: 36px; background: var(--brand-red); }

  .letterhead-footer { position: absolute; left: 0; right: 0; bottom: 0; height: 70px; background: var(--brand-red); color: var(--paper); font-family: var(--serif); font-style: italic; font-size: 12.5px; display: flex; flex-direction: column; justify-content: center; align-items: center; gap: 4px; }
  .letterhead-footer .sep { margin: 0 8px; opacity: .8; }

  .folder-logo { position: absolute; top: 250px; left: 0; right: 0; display: flex; justify-content: center; }
  .folder-logo .wordmark { color: var(--paper); font-size: 40px; gap: 12px; }
  .folder-logo .wordmark-dot { width: 34px; height: 34px; background: var(--paper); }

  .card { position: absolute; width: 340px; height: 196px; top: 690px; box-shadow: 0 5px 14px rgba(0,0,0,.18); overflow: hidden; }
  .card-front { left: 60px; display: flex; }
  .card-back { left: 430px; background: var(--brand-red); display: flex; align-items: center; justify-content: center; }

  .card-front-brand { width: 42%; background: var(--mist); display: flex; align-items: center; justify-content: center; }
  .card-front-brand .wordmark { color: var(--ink); font-size: 13px; gap: 5px; }
  .card-front-brand .wordmark-dot { width: 10px; height: 10px; background: var(--brand-red); }

  .card-front-details { flex: 1; background: var(--brand-red); color: var(--paper); font-family: var(--serif); padding: 34px 16px 0 20px; }
  .card-holder { font-size: 14px; text-transform: uppercase; letter-spacing: .5px; }
  .card-role { font-size: 10px; font-style: italic; margin-bottom: 16px; }
  .contact-list { list-style: none; font-size: 9.5px; line-height: 1.55; }
  .contact-list li { display: flex; align-items: flex-start; gap: 6px; }
  .contact-list svg { flex: none; width: 8px; height: 8px; margin-top: 3px; fill: var(--paper); }

  .card-back .wordmark { color: var(--paper); font-size: 22px; gap: 8px; }
  .card-back .wordmark-dot { width: 18px; height: 18px; background: var(--paper); }
</style>
</head>
<body>
<main class="canvas">

  <section class="sheet letterhead" aria-label="Letterhead">
    <header class="letterhead-logo">
      <div class="wordmark"><span class="wordmark-dot"></span><span>Harbourline Staffing</span></div>
    </header>
    <div class="letterhead-watermark" aria-hidden="true">
      <div class="wordmark"><span class="wordmark-dot"></span><span>Harbourline Staffing</span></div>
    </div>
    <footer class="letterhead-footer">
      <p>+61 8 5550 0199<span class="sep">|</span>+61 8 5550 1234<span class="sep">|</span>dana@harbourlinestaffing.com</p>
      <p>L 9, 40 Quayside Road West Perth<span class="sep">|</span>harbourlinestaffing.com</p>
    </footer>
  </section>

  <section class="sheet folder" aria-label="Presentation folder cover">
    <div class="folder-logo">
      <div class="wordmark"><span class="wordmark-dot"></span><span>Harbourline Staffing</span></div>
    </div>
  </section>

  <section class="card card-front" aria-label="Business card front">
    <div class="card-front-brand">
      <div class="wordmark"><span class="wordmark-dot"></span><span>Harbourline Staffing</span></div>
    </div>
    <div class="card-front-details">
      <p class="card-holder">Dana Whitfield</p>
      <p class="card-role">Director</p>
      <ul class="contact-list">
        <li><svg viewBox="0 0 10 10" aria-hidden="true"><path d="M2 0h2l1 3-1.5 1a6 6 0 0 0 2.5 2.5L7 5l3 1v2c0 1-1 2-2 2A8 8 0 0 1 0 2c0-1 1-2 2-2z"/></svg>+61 8 5550 0199</li>
        <li><svg viewBox="0 0 10 10" aria-hidden="true"><rect x="2" y="0" width="6" height="10" rx="1"/></svg>+61 8 5550 1234</li>
        <li><svg viewBox="0 0 10 10" aria-hidden="true"><path d="M0 2h10v6H0z M0 2l5 3 5-3" stroke="#c01d2e" stroke-width=".8"/></svg>dana@harbourlinestaffing.com</li>
        <li><svg viewBox="0 0 10 10" aria-hidden="true"><circle cx="5" cy="5" r="5"/></svg>www.harbourlinestaffing.com</li>
        <li><svg viewBox="0 0 10 10" aria-hidden="true"><path d="M5 0a3.5 3.5 0 0 1 3.5 3.5C8.5 6 5 10 5 10S1.5 6 1.5 3.5A3.5 3.5 0 0 1 5 0z"/></svg>L 9, 40 Quayside Road<br>West Perth</li>
      </ul>
    </div>
  </section>

  <section class="card card-back" aria-label="Business card back">
    <div class="wordmark"><span class="wordmark-dot"></span><span>Harbourline Staffing</span></div>
  </section>

</main>
</body>
</html>
```